Business Card Design

My company is a Consulting & Training company (Halvane Consulting and Training, LLC) specializing in Firearms Training, State of Florida Concealed Weapons Permit Course, and Tactical Equipment Consulting.

Industry/Entity Type

Business

Contact Information for Business Card

Dario Holtzmeyer
P.O. Box 417302
Aventura, FL 33917
(786)492-7318

```html
<!DOCTYPE html>
<html lang="en">
<head>
<meta charset="utf-8">
<title>Halvane Consulting and Training – Business Card</title>
<link rel="stylesheet" href="https://fonts.googleapis.com/css2?family=PT+Sans+Narrow:wght@400;700&display=swap">
<style>
  :root {
    --backdrop: #4a4a4c;
    --card-white: #ffffff;
    --ink-black: #0b0b0b;
    --accent-red: #c8202f;
    --text-white: #f4f4f4;
  }
  html, body {
    margin: 0;
    padding: 0;
    width: 1200px;
    height: 1000px;
    overflow: hidden;
    background: var(--backdrop);
  }
  .canvas {
    position: relative;
    width: 1200px;
    height: 1000px;
    font-family: "PT Sans Narrow", "Arial Narrow", sans-serif;
  }
  .card {
    position: absolute;
    width: 560px;
    height: 320px;
    background: var(--card-white);
    overflow: hidden;
    box-shadow: 0 6px 18px rgba(0,0,0,0.35);
  }
  .card-front { left: 80px; top: 110px; }
  .card-back  { left: 560px; top: 570px; }

  .card-shapes {
    position: absolute;
    inset: 0;
    width: 560px;
    height: 320px;
  }

  .company-name {
    position: absolute;
    left: 0;
    right: 0;
    top: 48px;
    margin: 0;
    text-align: center;
    font-weight: 700;
    font-size: 31px;
    letter-spacing: 0.2px;
    color: var(--ink-black);
    text-transform: uppercase;
  }
  .service-list {
    position: absolute;
    left: 150px;
    top: 222px;
    margin: 0;
    padding: 0;
    list-style: none;
    color: var(--text-white);
    font-size: 16px;
    line-height: 21px;
  }
  .service-list li:nth-child(2) { padding-left: 12px; }
  .service-list li:nth-child(3) { padding-left: 24px; }

  .person-name {
    position: absolute;
    right: 72px;
    top: 124px;
    margin: 0;
    font-weight: 400;
    font-size: 41px;
    letter-spacing: 0.4px;
    white-space: nowrap;
    color: var(--ink-black);
    text-transform: uppercase;
  }
  .contact-list {
    position: absolute;
    left: 220px;
    top: 218px;
    margin: 0;
    padding: 0;
    list-style: none;
    font-size: 15px;
    line-height: 21px;
    color: var(--ink-black);
  }
  .contact-list li {
    display: flex;
    align-items: center;
    gap: 7px;
  }
  .contact-icon { width: 12px; height: 12px; flex: none; }
</style>
</head>
<body>
<main class="canvas">

  <section class="card card-front" aria-label="Business card front">
    <svg class="card-shapes" viewBox="0 0 560 320" aria-hidden="true">
      <path d="M0,212 C140,182 300,112 560,128 L560,320 L0,320 Z" fill="var(--accent-red)"/>
      <path d="M0,219 C140,189 300,119 560,135 L560,320 L0,320 Z" fill="var(--ink-black)"/>
    </svg>
    <h1 class="company-name">Halvane Consulting and Training, LLC</h1>
    <ul class="service-list">
      <li>Firearms Training</li>
      <li>State of Florida Concealed Weapons Permit Course</li>
      <li>Tactical Equipment Consulting</li>
    </ul>
  </section>

  <section class="card card-back" aria-label="Business card back">
    <svg class="card-shapes" viewBox="0 0 560 320" aria-hidden="true">
      <rect x="0" y="58" width="338" height="52" fill="var(--accent-red)"/>
      <rect x="0" y="52" width="332" height="52" fill="var(--ink-black)"/>
      <rect x="508" y="170" width="52" height="40" fill="var(--accent-red)"/>
      <rect x="514" y="164" width="46" height="40" fill="var(--ink-black)"/>
    </svg>
    <h2 class="person-name">Dario Holtzmeyer</h2>
    <ul class="contact-list">
      <li>
        <svg class="contact-icon" viewBox="0 0 12 12" aria-hidden="true">
          <path d="M1,4 C1,2 3,1 6,1 C9,1 11,2 11,4 L9,5 L8,3.5 L4,3.5 L3,5 Z" fill="var(--accent-red)"/>
          <path d="M3,6 L9,6 L10.5,11 L1.5,11 Z" fill="var(--accent-red)"/>
          <circle cx="6" cy="8.5" r="1.3" fill="var(--card-white)"/>
        </svg>
        <span>(786)492-7318</span>
      </li>
      <li>
        <svg class="contact-icon" viewBox="0 0 12 12" aria-hidden="true">
          <path d="M6,0.5 C3.5,0.5 2,2.3 2,4.4 C2,7.3 6,11.5 6,11.5 C6,11.5 10,7.3 10,4.4 C10,2.3 8.5,0.5 6,0.5 Z" fill="var(--accent-red)"/>
          <circle cx="6" cy="4.4" r="1.5" fill="var(--card-white)"/>
        </svg>
        <span>P.O. Box 417302 Aventura, FL 33917</span>
      </li>
    </ul>
  </section>

</main>
</body>
</html>
```